Business Card Design For Marketing Agnecy LVT

Need business card design for marketing agency.

Dorian Pell
President, CEO
1-555-304-2917
dorian@lumenvaletrewards.net
www.LumenValeTrewards.biz

Back Side:
Boost Sales Using Rewards, Incentives & Giveaways
Get A Free Sample Package

Target Market(s)

B2B

Industry/Entity Type

Marketing

Contact Information for Business Card

Dorian Pell
President, CEO
1-555-304-2917

Back Side:
Get A Free Sample Package

Please note that my current url is OLD DESIGN. I am working on new design and want the business card to match color themes at least on new site. Here is the demo link for new site so you can see the colors I use, etc.

http://pagekilnstudio.example/qx/dorian/lvt_final/index.html

Requirements
Must have
• Please note that my current url is OLD DESIGN. I am working on new design and want the business card to match color themes at least on new site. Here is the demo link for new site so you can see the colors I use, etc.

Nice to have

Should not have

```html
<!DOCTYPE html>
<html lang="en">
<head>
<meta charset="utf-8">
<title>LVT Business Card</title>
<link rel="stylesheet" href="https://fonts.googleapis.com/css2?family=Roboto:wght@400;500;700;900&display=swap">
<style>
  :root {
    --brand-blue: #1f72c0;
    --brand-blue-dark: #1a63a8;
    --paper: #fbfbfb;
    --ink-grey: #55585c;
    --arc-grey: #4a4c50;
    --backdrop: #d9d9d7;
    --white: #ffffff;
  }
  * { box-sizing: border-box; margin: 0; padding: 0; }
  html, body { width: 1200px; height: 810px; overflow: hidden; }
  body {
    background: var(--backdrop);
    font-family: "Roboto", Arial, sans-serif;
    position: relative;
  }
  .card {
    position: absolute;
    width: 540px;
    height: 309px;
    top: 250px;
    overflow: hidden;
    box-shadow: 0 6px 18px rgba(0,0,0,0.18);
  }
  .card-front { left: 30px; background: var(--paper); }
  .card-back { left: 630px; background: var(--brand-blue); }

  .front-shape { position: absolute; inset: 0; width: 100%; height: 100%; }

  .contact {
    position: absolute;
    left: 34px;
    top: 108px;
  }
  .contact-name {
    color: var(--brand-blue);
    font-weight: 700;
    font-size: 20px;
    line-height: 1.1;
  }
  .contact-title {
    color: var(--ink-grey);
    font-size: 13px;
    margin-top: 2px;
  }
  .contact-rule {
    width: 40px;
    height: 3px;
    background: var(--brand-blue);
    margin: 12px 0 12px 28px;
  }
  .contact-list { list-style: none; }
  .contact-list li {
    display: flex;
    align-items: center;
    gap: 8px;
    color: var(--ink-grey);
    font-size: 13px;
    line-height: 1.55;
  }
  .contact-icon {
    width: 14px;
    height: 14px;
    border-radius: 50%;
    background: var(--brand-blue);
    display: inline-flex;
    align-items: center;
    justify-content: center;
    flex: none;
  }
  .contact-icon svg { width: 9px; height: 9px; }

  .brand-mark {
    position: absolute;
    display: flex;
    align-items: center;
    gap: 10px;
    color: var(--white);
    font-weight: 900;
    letter-spacing: 2px;
  }
  .brand-mark-dot {
    background: var(--white);
    border-radius: 50%;
    flex: none;
  }
  .card-front .brand-mark { left: 355px; top: 106px; font-size: 60px; }
  .card-front .brand-mark-dot { width: 14px; height: 14px; }
  .card-back .brand-mark {
    left: 0; right: 0; top: 62px;
    justify-content: center;
    font-size: 92px;
  }
  .card-back .brand-mark-dot { width: 20px; height: 20px; }

  .offer {
    position: absolute;
    left: 0; right: 0;
    top: 208px;
    text-align: center;
    color: var(--white);
  }
  .offer-headline {
    font-size: 27px;
    font-weight: 400;
    letter-spacing: 0.5px;
    text-transform: uppercase;
  }
  .offer-headline strong { font-weight: 700; }
  .offer-tagline {
    font-size: 15px;
    font-style: normal;
    margin-top: 4px;
  }
</style>
</head>
<body>

  <section class="card card-front" aria-label="Business card front">
    <svg class="front-shape" viewBox="0 0 540 309" preserveAspectRatio="none" aria-hidden="true">
      <path d="M258 0 L540 0 L540 309 L225 309 C300 230 330 120 258 0 Z" fill="var(--brand-blue)"/>
      <path d="M258 0 C300 60 312 130 296 190 C316 130 306 60 272 0 Z" fill="var(--arc-grey)"/>
    </svg>

    <div class="contact">
      <p class="contact-name">Dorian Pell</p>
      <p class="contact-title">President, CEO</p>
      <div class="contact-rule"></div>
      <ul class="contact-list">
        <li>
          <span class="contact-icon"><svg viewBox="0 0 10 10"><path d="M2 1 L4 1 L4.6 3 L3.5 4 C4 5.3 4.8 6 6 6.5 L7 5.4 L9 6 L9 8 C5 8.5 1.5 5 2 1 Z" fill="#fff"/></svg></span>
          1-555-304-2917
        </li>
        <li>
          <span class="contact-icon"><svg viewBox="0 0 10 10"><rect x="1" y="2.5" width="8" height="5.5" fill="#fff"/><path d="M1 2.5 L5 5.5 L9 2.5" stroke="var(--brand-blue)" stroke-width="0.9" fill="none"/></svg></span>
          dorian@lumenvaletrewards.net
        </li>
        <li>
          <span class="contact-icon"><svg viewBox="0 0 10 10"><circle cx="5" cy="5" r="3.6" stroke="#fff" stroke-width="0.9" fill="none"/><path d="M1.4 5 H8.6 M5 1.4 C3 3.5 3 6.5 5 8.6 M5 1.4 C7 3.5 7 6.5 5 8.6" stroke="#fff" stroke-width="0.8" fill="none"/></svg></span>
          www.LumenValeTrewards.biz
        </li>
      </ul>
    </div>

    <div class="brand-mark"><span class="brand-mark-dot"></span>LVT</div>
  </section>

  <section class="card card-back" aria-label="Business card back">
    <div class="brand-mark"><span class="brand-mark-dot"></span>LVT</div>
    <div class="offer">
      <p class="offer-headline">Get a free <strong>sample package</strong></p>
      <p class="offer-tagline">Boost Sales Using Rewards, Incentives &amp; Giveaways</p>
    </div>
  </section>

</body>
</html>
```